Prospective Client Follow Up Marketing Mailer

This is a post card mailer used as a follow up touch point;providing information following contact via Chatter Hub or other introductory touch. Its a key piece in the solicitation strategy to stir interest in using Bramble Loss Partners. As a follow up piece it needs to provide the salient selling points as to why use, choose or select Bramble to handle claims.
This should draw the reader's/receiver's eye to the key points and establish I their mind why they should choose to use Bramble Loss Partners for handling their property claims. Why they should place Bramble Loss Partners on their carrier's roster fro claim assignments.
Updates

Target Market(s)

These cards are sent to vendor managers at insurance companies or staff adjuster that hand out claim assignments.

Industry/Entity Type

Insurance

Requirements
Must have
• Professional look, fresh graphics/art work with salient selling points listed. Clean look. Clear and concise.
• Contact information.
Should not have
• clutter, too much written information.

```html
<!DOCTYPE html>
<html lang="en">
<head>
<meta charset="utf-8">
<title>Bramble Loss Partners – Follow Up Mailer</title>
<link href="https://fonts.googleapis.com/css2?family=Roboto+Condensed:wght@400;700&family=Open+Sans:wght@400&display=swap" rel="stylesheet">
<style>
:root{
  --blue-dark:#0a5aa6;
  --blue-light:#1d92d0;
  --navy:#15346a;
  --ink:#1f1f1f;
  --grey-text:#333;
  --charcoal:#333536;
  --footer:#6b6c6e;
  --cream:#f7f1e6;
  --panel:#f1f2f3;
  --page:#e9e9e9;
}
*{margin:0;padding:0;box-sizing:border-box}
html,body{width:1200px;height:1200px;overflow:hidden;background:var(--page)}
.canvas{position:relative;width:1200px;height:1200px}
.card{position:absolute;width:874px;height:632px;transform-origin:0 0;transform:scale(.857);background:#fff;overflow:hidden;box-shadow:0 2px 6px rgba(0,0,0,.25);font-family:"Roboto Condensed",sans-serif}
.card--front{left:225px;top:44px}
.card--back{left:225px;top:615px}
.art{position:absolute;left:0;top:0}
.brand{position:absolute;left:36px;top:48px;display:flex;align-items:center;gap:10px}
.brand__mark{width:22px;height:22px;background:var(--blue-dark)}
.brand__name{font-size:26px;font-weight:700;color:var(--blue-dark);letter-spacing:.5px}
.headline{position:absolute;left:57px;top:386px;line-height:1}
.headline__big{font-size:52px;font-weight:700;color:var(--ink);letter-spacing:.5px}
.headline__l1{font-size:29px;color:var(--grey-text);margin-top:6px}
.headline__l2{font-size:32px;font-weight:700;color:var(--navy);margin-top:2px}
.headline__l3{font-size:37px;font-weight:700;color:var(--ink);margin-top:6px}
.contact{position:absolute;display:flex;align-items:center;gap:8px;font-size:17px;color:var(--ink);white-space:nowrap}
.icon{width:23px;height:23px;border-radius:50%;background:var(--blue-dark);display:inline-flex;align-items:center;justify-content:center;flex:none}
.icon svg{width:14px;height:14px}
.panel{position:absolute;left:0;top:0;width:487px;height:632px;background:linear-gradient(180deg,#fff 0%,var(--panel) 100%)}
.services__title{position:absolute;left:46px;top:76px;font-size:21px;font-weight:700;color:var(--ink)}
.service{position:absolute;left:46px;width:400px}
.service__name{display:flex;align-items:center;gap:8px;font-size:18px;color:var(--blue-dark)}
.service__desc{margin-left:32px;font-family:"Open Sans",sans-serif;font-size:14.5px;line-height:18px;color:var(--ink);text-align:justify}
.footer{position:absolute;left:0;top:536px;width:487px;height:96px;background:var(--footer);color:#fff;font-size:15.5px}
.footer .contact{color:#fff;font-size:15.5px;align-items:flex-start}
.stamp{position:absolute;left:740px;top:33px;width:100px;height:112px;border:1px solid #555}
.addr-line{position:absolute;left:519px;width:322px;height:1px;background:#555}
</style>
</head>
<body>
<div class="canvas">

  <section class="card card--front">
    <svg class="art" width="874" height="632" viewBox="0 0 874 632">
      <defs>
        <linearGradient id="creamFade" x1="0" y1="0" x2="1" y2="0">
          <stop offset="0" stop-color="#f8f1e4"/><stop offset="1" stop-color="#fbf7f0"/>
        </linearGradient>
        <linearGradient id="photoTone" x1="0" y1="0" x2="1" y2="1">
          <stop offset="0" stop-color="#d9d4cc"/><stop offset=".45" stop-color="#b9b4ae"/><stop offset="1" stop-color="#e7ecf2"/>
        </linearGradient>
      </defs>
      <rect width="874" height="632" fill="url(#creamFade)"/>
      <polygon points="215,0 874,0 874,400 720,560 170,210" fill="url(#photoTone)" role="img" aria-label="Photo: business professionals shaking hands across a glass meeting table"/>
      <polygon points="0,177 0,225 110,292 150,262" fill="var(--blue-light)"/>
      <polygon points="0,372 172,250 740,512 874,445 874,632 0,632" fill="#fff"/>
      <polygon points="0,328 167,183 760,487 740,512 172,250 0,372" fill="var(--blue-dark)"/>
      <polygon points="172,250 740,512 700,535 175,275" fill="var(--blue-light)"/>
      <polygon points="690,575 874,392 874,440 718,588" fill="var(--blue-light)"/>
      <polygon points="650,632 874,455 874,632" fill="var(--charcoal)"/>
    </svg>

    <div class="brand"><span class="brand__mark"></span><span class="brand__name">Bramble Loss Partners</span></div>

    <div class="headline">
      <div class="headline__big">BUILDING</div>
      <div class="headline__l1">trustworthy relationships</div>
      <div class="headline__l2">by delivering peace of mind</div>
      <div class="headline__l3">to our clients' insureds</div>
    </div>

    <div class="contact" style="left:56px;top:581px">
      <span class="icon"><svg viewBox="0 0 14 14"><circle cx="7" cy="7" r="5.5" fill="none" stroke="#fff" stroke-width="1.3"/><path d="M1.5 7h11M7 1.5c-3 3.5-3 7.5 0 11M7 1.5c3 3.5 3 7.5 0 11" fill="none" stroke="#fff" stroke-width="1.1"/></svg></span>
      www.bramblelosspartners.com
    </div>
    <div class="contact" style="left:372px;top:581px">
      <span class="icon"><svg viewBox="0 0 14 14"><path d="M3 1.5l2.2 2.6-1.2 1.5c.8 1.8 2.1 3.1 3.9 3.9l1.5-1.2 2.6 2.2-1.4 2C6 12 2 8 1 3z" fill="#fff"/></svg></span>
      818) 555-0142
    </div>
    <div class="contact" style="left:520px;top:581px">
      <span class="icon"><svg viewBox="0 0 14 14"><rect x="2" y="5" width="10" height="7" fill="#fff"/><rect x="4" y="2" width="6" height="4" fill="none" stroke="#fff" stroke-width="1.2"/></svg></span>
      (330) 555-0187
    </div>
  </section>

  <section class="card card--back">
    <div class="panel"></div>
    <svg class="art" width="487" height="100" viewBox="0 0 487 100">
      <polygon points="0,0 487,0 487,50 0,20" fill="var(--blue-dark)"/>
      <polygon points="0,20 130,0 150,0 0,72" fill="var(--blue-dark)"/>
      <polygon points="60,0 487,55 487,88 0,22 0,12" fill="var(--blue-light)"/>
    </svg>

    <div class="services__title">SERVICES</div>

    <div class="service" style="top:107px">
      <div class="service__name"><span class="icon"><svg viewBox="0 0 14 14"><path d="M7 2l5.5 5H11v5H3V7H1.5z" fill="#fff"/></svg></span>Property Adjusting</div>
      <div class="service__desc">Adjusting residential and commercial daily claims</div>
    </div>
    <div class="service" style="top:161px">
      <div class="service__name"><span class="icon"><svg viewBox="0 0 14 14"><circle cx="6" cy="6" r="3.5" fill="none" stroke="#fff" stroke-width="1.5"/><path d="M8.5 8.5l3.5 3.5" stroke="#fff" stroke-width="1.8"/></svg></span>Subrogation Investigations</div>
      <div class="service__desc">Assessing whether injury or property damage caused by another individual or company</div>
    </div>
    <div class="service" style="top:232px">
      <div class="service__name"><span class="icon"><svg viewBox="0 0 14 14"><circle cx="6" cy="6" r="4" fill="#fff"/><path d="M9 9l3.5 3.5" stroke="#fff" stroke-width="1.8"/></svg></span>AOE/COE Investigations</div>
      <div class="service__desc">Gathering all facts relevant to filing of a workers' compensation claim</div>
    </div>
    <div class="service" style="top:303px">
      <div class="service__name"><span class="icon"><svg viewBox="0 0 14 14"><rect x="2" y="4" width="8" height="4" fill="#fff" transform="rotate(20 6 6)"/><path d="M4 9v3" stroke="#fff" stroke-width="1.5"/></svg></span>Surveillance</div>
      <div class="service__desc">Obtaining video footage to assist in the mitigation of claim exposure</div>
    </div>
    <div class="service" style="top:381px">
      <div class="service__name"><span class="icon"><svg viewBox="0 0 14 14"><circle cx="7" cy="7" r="2.5" fill="#fff"/><circle cx="7" cy="7" r="5.2" fill="none" stroke="#fff" stroke-width="1.1"/></svg></span>Social Media</div>
      <div class="service__desc">Using technology and data base research to determine relevant information on an injured worker</div>
    </div>
    <div class="service" style="top:454px">
      <div class="service__name"><span class="icon"><svg viewBox="0 0 14 14"><path d="M2.5 2.5l9 9M11.5 2.5l-9 9" stroke="#fff" stroke-width="1.6"/></svg></span>Lien Negotiation Services</div>
      <div class="service__desc">Negotiating workers' compensation lien issues (California) to reduce loss cost exposure on a claim file</div>
    </div>

    <div class="footer">
      <div class="contact" style="left:46px;top:14px;line-height:18px">
        <span class="icon"><svg viewBox="0 0 14 14"><circle cx="7" cy="7" r="5.5" fill="none" stroke="#fff" stroke-width="1.3"/><path d="M1.5 7h11M7 1.5c-3 3.5-3 7.5 0 11M7 1.5c3 3.5 3 7.5 0 11" fill="none" stroke="#fff" stroke-width="1.1"/></svg></span>
        <span>4820 Orchard Ridge Blvd.<br>Suite 7, Fairview Hills, CA. 90210</span>
      </div>
      <div class="contact" style="left:46px;top:50px">
        <span class="icon"><svg viewBox="0 0 14 14"><circle cx="7" cy="7" r="5.5" fill="none" stroke="#fff" stroke-width="1.3"/><path d="M1.5 7h11M7 1.5c-3 3.5-3 7.5 0 11M7 1.5c3 3.5 3 7.5 0 11" fill="none" stroke="#fff" stroke-width="1.1"/></svg></span>
        www.bramblelosspartners.com
      </div>
      <div class="contact" style="left:320px;top:16px">
        <span class="icon"><svg viewBox="0 0 14 14"><path d="M3 1.5l2.2 2.6-1.2 1.5c.8 1.8 2.1 3.1 3.9 3.9l1.5-1.2 2.6 2.2-1.4 2C6 12 2 8 1 3z" fill="#fff"/></svg></span>
        818) 555-0142
      </div>
      <div class="contact" style="left:320px;top:46px">
        <span class="icon"><svg viewBox="0 0 14 14"><rect x="2" y="5" width="10" height="7" fill="#fff"/><rect x="4" y="2" width="6" height="4" fill="none" stroke="#fff" stroke-width="1.2"/></svg></span>
        (330) 555-0187
      </div>
    </div>

    <div class="stamp"></div>
    <div class="addr-line" style="top:362px"></div>
    <div class="addr-line" style="top:421px"></div>
    <div class="addr-line" style="top:475px"></div>
    <div class="addr-line" style="top:534px"></div>
  </section>

</div>
</body>
</html>
```